Business Card design for construction company

I would like a business card design for a construction company - Harlow Constructions. I have attached the ai logo file for use. I would like the card to be very smart and clean and incorporate only white and the two colours in the logo. I would like the card to have two sides. One side can just have the logo, the other with the relevant information.

Target Market(s)

Building and Construction Clients

Industry/Entity Type

Business

Contact Information for Business Card

Name: Tom Pardoe
Company: Harlow Constructions Pty Limited
Address: 14 Mallee Crescent Carrow Vale 2093
Phone: 0427 531 068
Email: tomp@harlowbuild-example.com.au

Font styles to use
Serif
Sans Serif

Requirements
Must have
• Details noted above
• Logo as provided
• Colours as in logo
• Square edges
• A font that compliments the logo
Should not have
• Any colour other than white and those in logo
• Rounded edges

```html
<!DOCTYPE html>
<html lang="en">
<head>
<meta charset="utf-8">
<title>Harlow Constructions – Business Card</title>
<link href="https://fonts.googleapis.com/css2?family=Open+Sans:wght@400;600&display=swap" rel="stylesheet">
<style>
  :root {
    --bg: #e9ebee;
    --white: #ffffff;
    --blue: #0aa0e2;
    --charcoal: #555657;
    --shadow: rgba(0, 0, 0, 0.18);
  }
  * { margin: 0; padding: 0; box-sizing: border-box; }
  html, body {
    width: 1200px;
    height: 900px;
    overflow: hidden;
    background: var(--bg);
    font-family: "Open Sans", Arial, sans-serif;
  }
  .canvas {
    position: relative;
    width: 1200px;
    height: 900px;
    display: flex;
    align-items: center;
    justify-content: center;
    gap: 50px;
  }
  .card {
    position: relative;
    width: 525px;
    height: 300px;
    box-shadow: 0 6px 18px var(--shadow);
    overflow: hidden;
  }

  /* Information side */
  .card--details { background: var(--white); }
  .name-block {
    position: absolute;
    left: 0;
    top: 70px;
    width: 168px;
    height: 152px;
    background: var(--blue);
  }
  .name-block__name {
    position: absolute;
    left: 18px;
    top: 16px;
    color: var(--white);
    font-weight: 600;
    font-size: 22px;
    line-height: 1.1;
    white-space: nowrap;
  }
  .info-band {
    position: absolute;
    left: 168px;
    right: 0;
    top: 70px;
    height: 152px;
    background: var(--charcoal);
    color: var(--white);
    padding: 22px 0 0 40px;
    font-size: 12.5px;
    line-height: 1.45;
  }
  .info-band__rule {
    position: absolute;
    left: 22px;
    top: 22px;
    width: 1.5px;
    height: 108px;
    background: var(--white);
  }
  .info-band__address { margin-bottom: 8px; }
  .contact-line { display: flex; align-items: center; gap: 7px; }
  .contact-line svg { width: 11px; height: 11px; flex: none; }

  /* Logo side */
  .card--brand {
    background: var(--charcoal);
    display: flex;
    align-items: center;
    justify-content: center;
    gap: 18px;
  }
  .brand-name {
    display: flex;
    align-items: center;
    gap: 7px;
    color: var(--white);
    font-weight: 400;
    font-size: 30px;
    letter-spacing: 1px;
  }
  .brand-name__square {
    width: 7px;
    height: 7px;
    background: var(--blue);
  }
  .brand-divider {
    width: 1.5px;
    height: 50px;
    background: var(--blue);
  }
  .brand-descriptor {
    color: var(--white);
    font-size: 19px;
    letter-spacing: 4px;
    text-transform: uppercase;
  }
</style>
</head>
<body>
<main class="canvas">

  <section class="card card--details" aria-label="Business card, contact side">
    <div class="name-block">
      <p class="name-block__name">Tom Pardoe</p>
    </div>
    <div class="info-band">
      <span class="info-band__rule"></span>
      <p class="info-band__address">
        Harlow Constructions Pty Limited<br>
        14 Mallee Crescent<br>
        Carrow Vale 2093
      </p>
      <p class="contact-line">
        <svg viewBox="0 0 12 12" aria-hidden="true"><path d="M2.5 1 L4.5 1 L5.3 3.4 L4 4.4 Q5 6.8 7.6 8 L8.6 6.7 L11 7.5 L11 9.5 Q10.5 11 9 11 Q1 10 1 2.5 Q1 1 2.5 1 Z" fill="var(--blue)"/></svg>
        0427 531 068
      </p>
      <p class="contact-line">
        <svg viewBox="0 0 12 12" aria-hidden="true"><rect x="0.5" y="2" width="11" height="8" fill="var(--blue)"/><path d="M0.5 2 L6 6.5 L11.5 2" fill="none" stroke="var(--white)" stroke-width="1"/></svg>
        tomp@harlowbuild-example.com.au
      </p>
    </div>
  </section>

  <section class="card card--brand" aria-label="Business card, logo side">
    <div class="brand-name">
      <span class="brand-name__square"></span>
      <span>Harlow</span>
    </div>
    <span class="brand-divider"></span>
    <span class="brand-descriptor">Constructions</span>
  </section>

</main>
</body>
</html>
```